Electrician Letterhead Design RMV

We need some letterhead for our bills and other papers.
Customer address is on the right side (Swiss format)
A4 format

Design should also be applicable on Cards

Target Market(s)

Private Customers, Small Business

Industry/Entity Type

Electrician

Other font styles liked:
• incised 901

Colors
00AB8E
00BBA5
67D7C9
C6EFE9
E9F9F6

```html
<!DOCTYPE html>
<html lang="en">
<head>
<meta charset="utf-8">
<title>RMV Letterhead</title>
<link rel="stylesheet" href="https://fonts.googleapis.com/css2?family=Open+Sans:wght@400;600;700&display=swap">
<style>
  :root {
    --canvas: #dcdcdc;
    --paper: #f8f8f8;
    --brand: #1a9e8c;
    --brand-band: #21a08f;
    --ink: #111111;
    --text: #666666;
    --contact: #555555;
    --signature-tone: #e6e9ee;
  }
  * { box-sizing: border-box; margin: 0; padding: 0; }
  html, body {
    width: 1153px;
    height: 1200px;
    overflow: hidden;
    background: var(--canvas);
  }
  body { position: relative; font-family: "Open Sans", Arial, sans-serif; }
  .letterhead {
    position: absolute;
    left: 167px;
    top: 30px;
    width: 818px;
    height: 1140px;
    background: var(--paper);
    box-shadow: 0 8px 24px rgba(0,0,0,0.12);
  }
  .brand {
    position: absolute;
    left: 81px;
    top: 58px;
  }
  .brand-name {
    font-size: 72px;
    font-weight: 700;
    line-height: 1;
    color: var(--brand);
    letter-spacing: 1px;
  }
  .brand-company {
    margin-top: 6px;
    font-size: 11px;
    font-weight: 600;
    color: var(--ink);
    letter-spacing: 0.3px;
  }
  .contact {
    position: absolute;
    left: 541px;
    top: 64px;
    font-size: 14px;
    line-height: 16.5px;
    color: var(--contact);
    list-style: none;
  }
  .contact-address { margin-bottom: 8px; }
  .contact-line { display: flex; align-items: center; gap: 6px; }
  .contact-line svg { width: 13px; height: 13px; fill: var(--brand); flex: none; }
  .letter {
    position: absolute;
    left: 81px;
    top: 282px;
    width: 656px;
    font-size: 14.6px;
    line-height: 21.5px;
    color: var(--text);
  }
  .letter p { margin-bottom: 21.5px; }
  .letter .body-text { text-align: justify; }
  .signature {
    width: 94px;
    height: 90px;
    margin-top: 16px;
    border-radius: 4px;
    background: linear-gradient(135deg, var(--signature-tone), var(--paper));
  }
  .footer-band {
    position: absolute;
    left: 0;
    bottom: 0;
    width: 818px;
    height: 15px;
  }
</style>
</head>
<body>
  <main class="letterhead">
    <header class="brand">
      <div class="brand-name">RMV</div>
      <div class="brand-company">Rheinwald Montage Volt GmbH</div>
    </header>

    <address class="contact">
      <div class="contact-address">Lindenweg 14 04103<br>City Talheim Germany</div>
      <div class="contact-line">
        <svg viewBox="0 0 16 16" aria-hidden="true"><path d="M2 6c0-2 3-3 6-3s6 1 6 3v1h-3V5.5c-1-.4-2-.5-3-.5s-2 .1-3 .5V7H2zM4 8h8l2 5H2z"/></svg>
        555.204.3178
      </div>
      <div class="contact-line">
        <svg viewBox="0 0 16 16" aria-hidden="true"><path d="M1 3h14v2L8 9 1 5zM1 7l7 4 7-4v6H1z"/></svg>
        info@rmv-elektro .com
      </div>
      <div class="contact-line">
        <svg viewBox="0 0 16 16" aria-hidden="true"><circle cx="8" cy="8" r="7"/><path d="M5 4c2 0 2 2 4 2s0 3-2 3-1 3-3 2-1-4-1-5 1-2 2-2zM11 9c1 0 2 1 1 3-1 1-2 0-2-1s0-2 1-2z" fill="#f8f8f8"/></svg>
        www.rmv-elektro .com
      </div>
    </address>

    <section class="letter">
      <p>Dear customer,</p>
      <p class="body-text">Lorem ipsum dolor sit amet, consectetur adipisicing elit, sed do eiusmod tempor incididunt ut labore et dolore magna aliqua. Ut enim ad minim veniam, quis nostrud exercitation ullamco laboris nisi ut aliquip ex ea commodo consequat. Duis aute irure dolor in reprehenderit in voluptate velit esse cillum dolore eu fugiat nulla pariatur. Excepteur sint occaecat cupidatat non proident, sunt in culpa qui officia deserunt mollit anim id est laborum.</p>
      <p class="body-text">Lorem ipsum dolor sit amet, consectetur adipisicing elit, sed do eiusmod tempor incididunt ut labore et dolore magna aliqua. Ut enim ad minim veniam, quis nostrud exercitation ullamco laboris nisi ut aliquip ex ea commodo consequat. Duis aute irure dolor in reprehenderit in voluptate velit esse cillum dolore eu fugiat nulla pariatur. Excepteur sint occaecat cupidatat non proident, sunt in culpa qui officia deserunt mollit anim id est laborum.</p>
      <p class="body-text">Lorem ipsum dolor sit amet, consectetur adipisicing elit, sed do eiusmod tempor incididunt ut labore et dolore magna aliqua. Ut enim ad minim veniam, quis nostrud exercitation ullamco laboris nisi ut aliquip ex ea commodo consequat. Duis aute irure dolor in reprehenderit in voluptate velit esse cillum dolore eu fugiat nulla pariatur. Excepteur sint occaecat cupidatat non proident, sunt in culpa qui officia deserunt mollit anim id est laborum.</p>
      <p class="body-text">Lorem ipsum dolor sit amet, consectetur adipisicing elit, sed do eiusmod tempor incididunt ut labore et dolore magna aliqua. Ut enim ad minim veniam, quis nostrud exercitation ullamco laboris nisi ut aliquip ex ea commodo consequat. Duis aute irure dolor in reprehenderit.</p>
      <p style="margin-bottom:0">Yours Sincerely,</p>
      <div class="signature" role="img" aria-label="Handwritten signature of the sender"></div>
    </section>

    <svg class="footer-band" viewBox="0 0 818 15" preserveAspectRatio="none" aria-hidden="true">
      <polygon points="0,0 546,0 520,15 0,15" fill="var(--brand-band)"/>
      <polygon points="554,0 818,0 818,15 528,15" fill="var(--ink)"/>
    </svg>
  </main>
</body>
</html>
```